Plakat-Design: Hausmesse Robotik und Cobots
Zielgruppe
High-Tech Engineering aus Euskirchen
Die KW Konstrukteure & Fachservice GmbH mit Sitz in Euskirchen entwickelt moderne Maschinen Robotiklösungen für Kunden in der Region, überregional und bundesweit. Mittelständische Unternehmen und Maschinenbauer, internationale Großkonzerne aus der Konsumgüterindustrie und Hersteller von Maschinen für die weiterverarbeitende Industrie vertrauen KW seit vielen Jahren.
> Maschinenbau
> Automation
> Robotik
> Certified Systemintegrator für Brennwald Mechatronik
Aufgabenstellung
Projektauftrag:
Flyer/Plakat zur Einladung Hausmesse
Format:
> Din A4 PDF zur Einladung der Kunten (digital)
> Werbebanner für E-Mail Signatur
Daten der Messe:
> 18.05.2022 10-17 Uhr
> KW Technik , Lindenhofer Weg 14, 53879 Euskirchen
> Anmeldeplattform folgt
Motto der Veranstaltung:
> 'Automation - so einfach'
> 'Einfach automatisieren mit Cobots'
> Für Vorschläge gerne offen
Was erwartet Sie:
> Roboter Demos
> Kamerageführte Robotik
> Plug & Play Lösungen
Ausstellerinformationen:
> Bitte unten Platz für Logos der Aussteller vorsehen (derzeit ca. 15)
> Logos können später übermittelt werden
Infomaterial für den Designer:
>> www.kw-technik-beispiel.de
>> www.brennwald-mechatronik-beispiel.de
>> Weitere Bilder sind vorhanden.
>> Farbeschema der PowerPoint nutzen (Vertriebspräsentation_de_KW_21-06-23.pptx)

```html
<!DOCTYPE html>
<html lang="de">
<head>
<meta charset="utf-8">
<title>Hausmesse – Automation so einfach</title>
<link href="https://fonts.googleapis.com/css2?family=Baloo+2:wght@700&family=Montserrat:wght@400&family=Roboto:wght@400;500;700&display=swap" rel="stylesheet">
<style>
  :root{
    --brand-blue:#2e4a96;
    --brand-blue-deep:#1f3b8c;
    --ink:#111111;
    --dark-band:#262626;
    --grey-text:#4a4a4a;
    --client-grey:#a3a3a3;
    --ring:#c9d3e8;
    --paper:#ffffff;
  }
  html,body{margin:0;padding:0;width:1175px;height:1200px;overflow:hidden;background:var(--paper);}
  .poster{position:absolute;left:263px;top:109px;width:690px;height:976px;background:var(--paper);overflow:hidden;font-family:"Roboto",Arial,sans-serif;}
  .brand-mark{position:absolute;left:29px;top:39px;display:flex;align-items:center;gap:5px;font-family:"Roboto",Arial,sans-serif;font-weight:700;font-size:16px;line-height:20px;color:var(--brand-blue-deep);white-space:nowrap;}
  .brand-mark .square{width:12px;height:12px;background:var(--brand-blue-deep);flex:none;}
  .headline{position:absolute;left:150px;top:27px;font-family:"Baloo 2",Arial,sans-serif;font-weight:700;font-size:18px;line-height:23px;letter-spacing:-0.3px;white-space:nowrap;}
  .headline .company{color:var(--brand-blue-deep);}
  .headline .claim{color:var(--grey-text);}
  .contact{position:absolute;right:40px;top:42px;text-align:right;font-family:"Montserrat",Arial,sans-serif;font-size:13.5px;line-height:18px;color:#222;white-space:nowrap;}
  .hero-photo{position:absolute;left:0;top:116px;width:690px;height:363px;
    background:linear-gradient(100deg,#8e8f92 0%,#c9c9c9 22%,#a97a54 38%,#6c6f78 52%,#2c2f3a 62%,#3d56a0 78%,#a9acb4 100%);}
  .title-band{position:absolute;left:0;top:376px;width:515px;height:75px;background:rgba(46,74,150,0.93);}
  .title-band h1{margin:0;position:absolute;left:48px;top:19px;color:#fff;font-weight:700;font-size:33px;line-height:38px;letter-spacing:0.2px;white-space:nowrap;}
  .frame-line{position:absolute;left:0;top:0;}
  .subtitle-band{position:absolute;left:0;top:451px;width:478px;height:58px;background:var(--dark-band);}
  .subtitle-band p{margin:0;position:absolute;left:48px;top:16px;color:#fff;font-weight:500;font-size:23px;line-height:26px;white-space:nowrap;}
  .deco-ring{position:absolute;left:510px;top:462px;}
  .features{position:absolute;left:0;top:564px;width:308px;}
  .feature{position:absolute;left:0;width:308px;height:46px;background:var(--brand-blue);color:#fff;display:flex;align-items:center;font-size:16px;}
  .feature svg{margin-left:49px;margin-right:12px;}
  .event{position:absolute;left:345px;top:562px;white-space:nowrap;}
  .event h2{margin:0;font-weight:700;font-size:23px;line-height:26px;color:var(--ink);}
  .event .strong{font-weight:500;color:var(--brand-blue);font-size:16.5px;line-height:22px;}
  .event .plain{color:var(--brand-blue);font-size:16.5px;line-height:22px;}
  .event .block{margin-bottom:20px;}
  .partners-label{position:absolute;left:52px;top:782px;font-size:14.5px;color:var(--brand-blue);}
  .clients{position:absolute;left:0;top:0;}
  .client{position:absolute;display:flex;align-items:center;gap:4px;font-size:10px;font-weight:500;color:var(--client-grey);}
  .client i{display:block;width:13px;height:13px;border-radius:50%;background:var(--client-grey);}
</style>
</head>
<body>
<div class="poster">
  <div class="brand-mark"><span class="square"></span>KW Technik</div>
  <div class="headline">
    <div class="company">KW Konstrukteure &amp; Fachservice -</div>
    <div class="claim">Wir realisieren Ihre Projekte</div>
  </div>
  <div class="contact">t. 49 2251 4820 0<br>e. info@kw-technik-beispiel.de</div>

  <div class="hero-photo" role="img" aria-label="Foto: kollaborativer Roboterarm mit Kamera und Greifer in einer Werkhalle"></div>

  <svg class="frame-line" width="690" height="500" aria-hidden="true">
    <polyline points="410,375 517,374 517,430" fill="none" stroke="#fff" stroke-width="1.5"/>
  </svg>

  <div class="title-band"><h1>AUTOMATION - SO EINFACH</h1></div>
  <div class="subtitle-band"><p>Einfach automatisieren mit Cobots</p></div>

  <svg class="deco-ring" width="180" height="190" aria-hidden="true">
    <circle cx="92" cy="93" r="62" fill="none" stroke="var(--ring)" stroke-width="1.3"/>
  </svg>

  <div class="features">
    <div class="feature" style="top:0">
      <svg width="20" height="20" viewBox="0 0 20 20"><circle cx="10" cy="10" r="8.5" fill="none" stroke="#fff" stroke-width="1.6"/><polyline points="6,10.3 9,13 14,7.2" fill="none" stroke="#fff" stroke-width="1.6"/></svg>Plug &amp; Play Lösungen</div>
    <div class="feature" style="top:60px">
      <svg width="20" height="20" viewBox="0 0 20 20"><circle cx="10" cy="10" r="8.5" fill="none" stroke="#fff" stroke-width="1.6"/><polyline points="6,10.3 9,13 14,7.2" fill="none" stroke="#fff" stroke-width="1.6"/></svg>Kamerageführte Robotik</div>
    <div class="feature" style="top:121px">
      <svg width="20" height="20" viewBox="0 0 20 20"><circle cx="10" cy="10" r="8.5" fill="none" stroke="#fff" stroke-width="1.6"/><polyline points="6,10.3 9,13 14,7.2" fill="none" stroke="#fff" stroke-width="1.6"/></svg>Roboter Demos</div>
  </div>

  <div class="event">
    <div class="block">
      <h2>WANN</h2>
      <div class="strong">18.05.2022</div>
      <div class="plain">10:00 - 17:00 Uhr</div>
    </div>
    <div class="block">
      <h2>WO</h2>
      <div class="strong">KW Technik</div>
      <div class="plain">Lindenhofer Weg 14 &nbsp; 53879 Euskirchen</div>
    </div>
  </div>

  <div class="partners-label">In Zusammenarbeit mit</div>
  <div class="clients">
    <div class="client" style="left:54px;top:829px"><i></i>Client</div>
    <div class="client" style="left:186px;top:829px"><i></i>Client</div>
    <div class="client" style="left:317px;top:829px"><i></i>Client</div>
    <div class="client" style="left:449px;top:829px"><i></i>Client</div>
    <div class="client" style="left:581px;top:829px"><i></i>Client</div>
    <div class="client" style="left:54px;top:871px"><i></i>Client</div>
    <div class="client" style="left:186px;top:871px"><i></i>Client</div>
    <div class="client" style="left:317px;top:871px"><i></i>Client</div>
    <div class="client" style="left:449px;top:871px"><i></i>Client</div>
    <div class="client" style="left:581px;top:871px"><i></i>Client</div>
    <div class="client" style="left:54px;top:913px"><i></i>Client</div>
    <div class="client" style="left:186px;top:913px"><i></i>Client</div>
    <div class="client" style="left:317px;top:913px"><i></i>Client</div>
    <div class="client" style="left:449px;top:913px"><i></i>Client</div>
    <div class="client" style="left:581px;top:913px"><i></i>Client</div>
  </div>
</div>
</body>
</html>
```